Corporate Design für Make Up Artist
Zielgruppe
Ich bin Make-up Artist und arbeite sehr viel B2B, aber auch teilweise B2C.
Im B2C Bereich ist meine Zielgruppe: Frauen im Alter von Ende 20 bis Ende 30, die sich gerne etwas gönnen, die viel Wert auf Schönheit legen und dabei nicht auf den Preis schauen, womit ich mich auch deutlich abheben möchte.
Im B2B sind es Geschäftskunden, die auf den ersten Blick meine Professionalität erkennen sollen.
Aufgabenstellung
Ich suche ein hochwertiges Design, das meine professionelle Arbeit, Vertrauen, Modernität und Exklusivität widerspiegelt.
Der Name LUMORA setzt sich aus dem spanischen Wort `Viveza`(=Lebendigkeit) und meinem Vornamen Korinna zusammen.
Dabei sind die Logos von Duroque, Henri Lacombe und der Mirelle meine Vorbilder.
Ich möchte keinesfalls kindliche Verschnörkelungen oder ähnliches. Mein Logo soll ein Statement setzen und im Gedächtnis bleiben.
Zudem möchte ich in Zukunft eigene Produkte im Beauty Segment auf den Markt bringen.
Die Farben, die mich persönlich widerspiegeln sind schwarz und gold.
Ich habe ein Logo hochgeladen, dass mich sehr anspricht, wo aber der nötige USP fehlt.
Bin aber auch für andere Vorschläge offen.

```html
<!DOCTYPE html>
<html lang="de">
<head>
<meta charset="utf-8">
<title>LUMORA Beauty – Visitenkarte und Namenszug</title>
<link rel="stylesheet" href="https://fonts.googleapis.com/css2?family=Noto+Serif:wght@400&display=swap">
<style>
  :root {
    --frame: #ffffff;
    --frame-line: #9a9a9a;
    --stage-light: #e4e2da;
    --stage-dark: #a9a79f;
    --night: #000000;
    --card-dark: #2f2f2f;
    --card-mid: #4a4a4a;
    --gold-deep: #b8901f;
    --gold: #d9b634;
    --gold-light: #ecd04e;
    --ink-light: #f4f4f2;
    --ink-soft: #d8d8d4;
  }
  * { box-sizing: border-box; margin: 0; padding: 0; }
  html, body { width: 1200px; height: 1200px; overflow: hidden; }
  body {
    background: var(--frame);
    border: 1px solid var(--frame-line);
    position: relative;
    font-family: "Noto Serif", serif;
    font-weight: 400;
  }
  .stage {
    position: absolute; left: 15px; top: 15px; width: 1168px; height: 728px;
    background: radial-gradient(ellipse at 35% 40%, var(--stage-light) 0%, #cfccc3 55%, var(--stage-dark) 100%);
  }
  .card {
    position: absolute; width: 500px; height: 286px; border-radius: 16px;
    background: linear-gradient(115deg, var(--card-dark) 0%, #393939 45%, var(--card-mid) 100%);
    box-shadow: 0 18px 30px rgba(0,0,0,0.35);
    color: var(--ink-light);
    overflow: hidden;
  }
  .card--front { left: 60px; top: 220px; }
  .card--back { left: 608px; top: 220px; }

  .brand {
    display: flex; align-items: center; justify-content: center; gap: 10px;
    color: var(--ink-light); font-weight: 400; letter-spacing: 0;
  }
  .brand__square { background: var(--gold); flex: none; }

  .card__brand { position: absolute; top: 38px; left: 0; right: 0; font-size: 17px; }
  .card__brand .brand__square { width: 10px; height: 10px; }

  .card__name {
    position: absolute; top: 86px; width: 100%; text-align: center;
    font-size: 21px;
  }
  .card__role {
    position: absolute; top: 120px; width: 100%; text-align: center;
    font-size: 10px; color: var(--ink-soft);
  }
  .card__rule {
    position: absolute; left: 0; right: 0; top: 156px; height: 3px;
    background: linear-gradient(90deg, var(--gold-deep), var(--gold-light), var(--gold));
  }
  .card__divider {
    position: absolute; left: 249px; top: 180px; width: 3px; height: 72px;
    background: linear-gradient(180deg, var(--gold-light), var(--gold-deep));
    transform: skewX(-12deg);
  }
  .card__address, .card__contact {
    position: absolute; top: 186px; font-size: 13px; line-height: 1.45; font-style: normal;
  }
  .card__address { right: 272px; text-align: right; }
  .card__contact { left: 272px; text-align: left; }

  .card__lockup { position: absolute; inset: 0; font-size: 24px; }
  .card__lockup .brand__square { width: 12px; height: 12px; }

  .showcase {
    position: absolute; left: 15px; top: 743px; width: 1168px; height: 441px;
    background: var(--night);
  }
  .showcase__brand { position: absolute; inset: 0; font-size: 34px; gap: 16px; }
  .showcase__brand .brand__square { width: 18px; height: 18px; }
</style>
</head>
<body>
  <section class="stage">
    <article class="card card--front">
      <div class="brand card__brand"><span class="brand__square"></span><span>LUMORA Beauty</span></div>
      <div class="card__name">Korinna Halvern</div>
      <div class="card__role">Make-up Artist &amp; Hairstylist</div>
      <div class="card__rule"></div>
      <address class="card__address">Lindenweg 8<br>97810 Marktstein<br>Germany</address>
      <div class="card__divider"></div>
      <div class="card__contact">+49(0) 151 20483756<br>info@lumora.beauty.de<br>lumora.beauty</div>
    </article>

    <article class="card card--back">
      <div class="brand card__lockup"><span class="brand__square"></span><span>LUMORA Beauty</span></div>
    </article>
  </section>

  <section class="showcase">
    <div class="brand showcase__brand"><span class="brand__square"></span><span>LUMORA Beauty</span></div>
  </section>
</body>
</html>
```